ORVILMA card Technical Architecture

Hello everyone ORVILMA: It is a consulting firm in Architecture and Construction. I require a card duplexing, sober, elegant, classic but not boring. Update 1: Use the following data for the card. Name: Rodrigo Salinas Tomás Quevedo Position: COO Twitter: @orvilmaAT Homepage: orvilma.com home address not include the participation of all thank you.

Target Market(s)

Construction companies, Architects and Consulting Engineers

Industry/Entity Type

Consulting

Contact Information for Business Card

Los campos que debe tener:
Nombre, Cargo, email, homepage y twitter

Font styles to use
Serif
Sans Serif
Other font styles liked:
• Me gustan playfair display, open sans y roboto, pero estoy sujeto a sus propuestas

Requirements
Must have
• Colors: Present combined proposals in white, red, gray and black Update 1: The two names must be clearly differentiated from the two surnames
Nice to have
• They are free to present their best proposals. I will bring them immediate feedback to the extent you can go see their designs. Complete data for card and logo files will give the winner the

```html
<!DOCTYPE html>
<html lang="es">
<head>
<meta charset="utf-8">
<title>ORVILMA – Tarjetas</title>
<link rel="stylesheet" href="https://fonts.googleapis.com/css2?family=Lato:wght@300;400;700&display=swap">
<style>
  :root {
    --red: #a81e23;
    --black: #0d0d0d;
    --white: #ffffff;
    --gray: #555555;
    --rule: #e0e0e0;
    --sheet: #ffffff;
    --card-w: 356px;
    --card-h: 197px;
  }
  * { box-sizing: border-box; margin: 0; padding: 0; }
  html, body { width: 1200px; height: 1011px; overflow: hidden; background: var(--sheet); }
  body { position: relative; font-family: "Lato", sans-serif; }

  .card {
    position: absolute;
    width: var(--card-w);
    height: var(--card-h);
    overflow: hidden;
    box-shadow: 0 6px 18px rgba(0,0,0,0.18);
  }
  .card--black { background: var(--black); color: var(--white); }
  .card--white { background: var(--white); color: var(--red); }
  .card--red { background: var(--red); color: var(--white); }

  .pattern { position: absolute; left: 0; top: 0; width: 100%; height: 100%; }
  .pattern--black-outline { background: linear-gradient(160deg, #1e1e1e 0%, #0d0d0d 60%); }
  .pattern--black-solid { background: linear-gradient(160deg, #3a3a3a 0%, #141414 55%, #0d0d0d 100%); }
  .pattern--white-solid { background: linear-gradient(160deg, #c9c9c9 0%, #f2f2f2 55%, #ffffff 100%); }
  .pattern--white-outline { background: linear-gradient(160deg, #ececec 0%, #fafafa 55%, #ffffff 100%); }
  .pattern--red-solid { background: linear-gradient(160deg, #d7898c 0%, #b8474b 45%, #a81e23 100%); }
  .pattern--red-outline { background: linear-gradient(160deg, #b7393d 0%, #a81e23 60%); }

  .lockup {
    position: absolute;
    left: 48px;
    top: 124px;
    width: 186px;
    text-align: center;
  }
  .lockup__name {
    display: block;
    font-weight: 400;
    font-size: 24px;
    line-height: 1;
    letter-spacing: 0.28em;
    margin-right: -0.28em;
    padding-bottom: 4px;
    border-bottom: 1px solid currentColor;
  }
  .lockup__tagline {
    display: block;
    margin-top: 3px;
    font-size: 8px;
    letter-spacing: 0.24em;
    margin-right: -0.24em;
    white-space: nowrap;
  }

  /* Front side */
  .front__mark {
    position: absolute;
    left: 38px; top: 38px;
    width: 22px; height: 22px;
    background: var(--red);
  }
  .front__details { position: absolute; left: 29px; top: 90px; width: 150px; }
  .front__given { font-size: 12px; color: var(--gray); line-height: 1.2; }
  .front__surname { font-size: 12px; color: var(--red); line-height: 1.2; padding-bottom: 7px; border-bottom: 1px solid var(--rule); }
  .front__role { font-size: 12px; color: var(--red); padding: 7px 0; border-bottom: 1px solid var(--rule); }
  .front__contact { font-size: 8.5px; color: var(--gray); margin-top: 8px; white-space: nowrap; }

  .front__vertical {
    position: absolute;
    left: 238px;
    top: 83px;
    width: 156px;
    height: 34px;
    transform: rotate(-90deg);
    transform-origin: 50% 50%;
    color: var(--red);
    text-align: center;
  }
  .front__vertical-name {
    display: block;
    font-size: 22px;
    line-height: 1;
    letter-spacing: 0.3em;
    margin-right: -0.3em;
    padding-bottom: 3px;
    border-bottom: 1px solid currentColor;
    white-space: nowrap;
  }
  .front__vertical-tagline {
    display: block;
    margin-top: 3px;
    font-size: 7px;
    letter-spacing: 0.22em;
    margin-right: -0.22em;
    white-space: nowrap;
  }
</style>
</head>
<body>

  <!-- Row 1 -->
  <section class="card card--black" style="left:224px; top:42px;">
    <div class="pattern pattern--black-outline" role="img" aria-label="Patrón decorativo de velas en línea fina blanca"></div>
    <div class="lockup"><span class="lockup__name">ORVILMA</span><span class="lockup__tagline">ARQUITECTURA TÉCNICA</span></div>
  </section>

  <section class="card card--black" style="left:606px; top:42px;">
    <div class="pattern pattern--black-solid" role="img" aria-label="Patrón decorativo de velas blancas sólidas"></div>
    <div class="lockup"><span class="lockup__name">ORVILMA</span><span class="lockup__tagline">ARQUITECTURA TÉCNICA</span></div>
  </section>

  <!-- Row 2 -->
  <section class="card card--white" style="left:24px; top:274px;">
    <div class="pattern pattern--white-solid" role="img" aria-label="Patrón decorativo de velas negras sólidas"></div>
    <div class="lockup"><span class="lockup__name">ORVILMA</span><span class="lockup__tagline">ARQUITECTURA TÉCNICA</span></div>
  </section>

  <section class="card card--white" style="left:416px; top:274px;">
    <div class="front__mark"></div>
    <div class="front__details">
      <p class="front__given">Tomás Rodrigo</p>
      <p class="front__surname">Salinas Quevedo</p>
      <p class="front__role">Director de Operaciones</p>
      <p class="front__contact">@orvilmaAT - www.orvilma.com</p>
    </div>
    <div class="front__vertical">
      <span class="front__vertical-name">ORVILMA</span>
      <span class="front__vertical-tagline">ARQUITECTURA TÉCNICA</span>
    </div>
  </section>

  <section class="card card--white" style="left:812px; top:274px;">
    <div class="pattern pattern--white-outline" role="img" aria-label="Patrón decorativo de velas en línea fina negra"></div>
    <div class="lockup"><span class="lockup__name">ORVILMA</span><span class="lockup__tagline">ARQUITECTURA TÉCNICA</span></div>
  </section>

  <!-- Row 3 -->
  <section class="card card--red" style="left:222px; top:500px;">
    <div class="pattern pattern--red-solid" role="img" aria-label="Patrón decorativo de velas blancas sólidas"></div>
    <div class="lockup"><span class="lockup__name">ORVILMA</span><span class="lockup__tagline">ARQUITECTURA TÉCNICA</span></div>
  </section>

  <section class="card card--red" style="left:58px; top:739px;">
    <div class="pattern pattern--red-outline" role="img" aria-label="Patrón decorativo de velas en línea fina clara"></div>
    <div class="lockup"><span class="lockup__name">ORVILMA</span><span class="lockup__tagline">ARQUITECTURA TÉCNICA</span></div>
  </section>

  <!-- Duplex pair, flat -->
  <section class="card card--white" style="left:690px; top:530px;">
    <div class="pattern pattern--white-solid" role="img" aria-label="Patrón decorativo de velas negras sólidas"></div>
    <div class="lockup"><span class="lockup__name">ORVILMA</span><span class="lockup__tagline">ARQUITECTURA TÉCNICA</span></div>
  </section>

  <section class="card card--white" style="left:740px; top:765px;">
    <div class="front__mark"></div>
    <div class="front__details">
      <p class="front__given">Tomás Rodrigo</p>
      <p class="front__surname">Salinas Quevedo</p>
      <p class="front__role">Director de Operaciones</p>
      <p class="front__contact">@orvilmaAT - www.orvilma.com</p>
    </div>
    <div class="front__vertical">
      <span class="front__vertical-name">ORVILMA</span>
      <span class="front__vertical-tagline">ARQUITECTURA TÉCNICA</span>
    </div>
  </section>

</body>
</html>
```